Powerpoint presentation about personal finance

Investing 4$ per day is what has been required to become a millionaire by investing in the stock market from 1965 to 2015. Yet only 1% of the population is millionaire. This presentation is about the most common causes why people do not build significant wealth through their life. We intend to educate people with this presentation, but also build trust so they become client of our wealth management firm. Feel free to send us any question about this project.
Updates

Reason: I have uploaded the logo source file and an updated PPT file. Thanks

Target Market(s)

People with a willingness to save money between the age of 20 to 50 years old

Industry/Entity Type

Finance

Font styles to use
Sans Serif

Requirements
Must have
• We are looking at uniforming the design throughout the presentation with nice, classic tone colors, large font size as it needs to be visible 3 meters apart. The content of the presentation will be updated regularly.
Should not have
• cartoon style, not serious

```html
<!DOCTYPE html>
<html lang="fr">
<head>
<meta charset="utf-8">
<title>Norvale – Présentation finances personnelles</title>
<link href="https://fonts.googleapis.com/css2?family=Open+Sans:wght@400;600;700&display=swap" rel="stylesheet">
<style>
:root{
  --blue:#1d6fb6;
  --blue-dark:#15558d;
  --green:#3fae4a;
  --green-dark:#2f8f3a;
  --ink:#33404d;
  --muted:#6b7681;
  --paper:#f3f4f6;
  --white:#ffffff;
  --line:#d7dbe0;
  --photo-a:#8fa3b6;
  --photo-b:#c9d3dc;
}
*{box-sizing:border-box;margin:0;padding:0}
html,body{width:1200px;height:3830px;overflow:hidden;background:var(--white)}
body{font-family:"Open Sans",Arial,sans-serif;color:var(--ink)}
.deck{
  display:grid;grid-template-columns:repeat(3,384px);grid-template-rows:repeat(13,284px);
  column-gap:12px;row-gap:10px;padding:9px 12px;width:1200px;height:3830px;
}
.slide{position:relative;overflow:hidden;background:var(--paper);border:1px solid var(--line)}
.slide-head{display:flex;justify-content:space-between;align-items:flex-start;padding:10px 14px 0 14px;height:44px}
.slide-head h2{font-size:14px;font-weight:600;color:var(--ink);line-height:1.2;max-width:260px}
.slide-head h2.long{font-size:11.5px;max-width:275px}
.slide-head::after{content:"";position:absolute;left:14px;right:14px;top:44px;height:1px;background:var(--line)}
.brand{display:flex;align-items:center;gap:4px;font-size:10px;font-weight:700;color:var(--blue);letter-spacing:.5px;white-space:nowrap}
.brand .dot{width:9px;height:9px;border-radius:50%;background:var(--green)}
.brand.lg{font-size:20px;gap:8px}
.brand.lg .dot{width:18px;height:18px}
.brand.on-dark{color:var(--white)}
.slide-body{position:absolute;left:14px;right:14px;top:54px;bottom:20px;font-size:9.5px;line-height:1.4}
.slide-foot{position:absolute;left:0;right:0;bottom:0;height:14px;padding:0 10px;font-size:6px;line-height:11px;color:var(--muted);border-top:3px solid var(--green);background:var(--white)}
.slide-foot.dark{background:var(--blue-dark);color:#cfe0ee}
.photo{background:linear-gradient(160deg,var(--photo-b),var(--photo-a))}
.photo.blue{background:linear-gradient(160deg,#6f9cc8,#1d4f80)}
.photo.grey{background:linear-gradient(160deg,#dfe3e7,#9aa6b1)}
.fill-blue{background:var(--blue);color:var(--white)}
.fill-green{background:var(--green);color:var(--white)}
.center-text{display:flex;align-items:center;justify-content:center;text-align:center}
.big-quote{font-size:12px;line-height:1.45;color:var(--ink);text-align:center}
p+p{margin-top:6px}
ul.list{list-style:none}
ul.list li{padding-left:10px;position:relative;margin-bottom:3px}
ul.list li::before{content:"";position:absolute;left:0;top:5px;width:4px;height:4px;background:var(--green)}
.num-item{display:flex;align-items:center;gap:8px;margin-bottom:8px}
.num{width:18px;height:18px;border-radius:50%;background:var(--blue);color:var(--white);font-size:9px;font-weight:700;display:flex;align-items:center;justify-content:center;flex:none}
.num.green{background:var(--green)}
.icon-item{display:flex;gap:6px;font-size:7.5px;line-height:1.3}
.icon-item .num{width:16px;height:16px}
.caps{text-transform:uppercase;font-weight:600}
.note{font-size:8px;color:var(--green-dark);font-weight:600}
.side-panel{position:absolute;top:0;bottom:14px;padding:16px}
</style>
</head>
<body>
<main class="deck">

<!-- Row 1 -->
<section class="slide">
  <div class="photo grey" role="img" aria-label="Photo de couverture pâle d'une ligne d'horizon urbaine" style="position:absolute;inset:0 0 14px 0;opacity:.6"></div>
  <footer class="slide-foot">© Copyright 2016 Norvale. Tous droits réservés.</footer>
</section>

<section class="slide" style="background:var(--white)">
  <div class="brand lg" style="position:absolute;top:48px;left:0;right:0;justify-content:center"><span class="dot"></span>NORVALE</div>
  <div class="fill-blue caps" style="position:absolute;left:0;right:0;top:118px;padding:14px 22px;font-size:10.5px;line-height:1.4">L'idéal pour beaucoup d'entre nous n'est-il pas d'avoir suffisamment d'argent et d'être en santé afin de pouvoir réaliser nos rêves?</div>
  <div class="fill-green" style="position:absolute;right:22px;top:196px;padding:2px 8px;font-size:7px">Octobre 18, 2016</div>
  <footer class="slide-foot">© Copyright 2016 Norvale. Tous droits réservés.</footer>
</section>

<section class="slide" style="background:var(--white)">
  <div class="photo blue" role="img" aria-label="Silhouettes de gens d'affaires devant des gratte-ciel" style="position:absolute;left:0;right:0;top:0;height:120px"></div>
  <div style="position:absolute;left:40px;top:22px;background:var(--white);padding:8px 14px"><div class="brand lg"><span class="dot"></span>NORVALE</div></div>
  <div class="caps" style="position:absolute;left:22px;right:22px;top:150px;font-size:10.5px;line-height:1.45;color:var(--blue)">L'idéal pour beaucoup d'entre nous n'est-il pas d'avoir suffisamment d'argent et d'être en santé afin de pouvoir réaliser nos rêves?</div>
  <footer class="slide-foot">© Copyright 2016 Norvale. Tous droits réservés.</footer>
</section>

<!-- Row 2 -->
<section class="slide">
  <header class="slide-head"><h2>Our Agenda</h2><div class="brand"><span class="dot"></span>NORVALE</div></header>
  <div class="slide-body" style="display:grid;grid-template-columns:1fr 1fr;gap:10px 14px;padding-top:10px">
    <div class="num-item"><span class="num">1</span><div><b style="color:var(--blue)">Agenda One</b><br><span style="font-size:7px;color:var(--muted)">Sujet principal de la section</span></div></div>
    <div class="num-item"><span class="num">4</span><div><b style="color:var(--blue)">Agenda Four</b><br><span style="font-size:7px;color:var(--muted)">Sujet principal de la section</span></div></div>
    <div class="num-item"><span class="num">2</span><div><b style="color:var(--blue)">Agenda Two</b><br><span style="font-size:7px;color:var(--muted)">Sujet principal de la section</span></div></div>
    <div class="num-item"><span class="num">5</span><div><b style="color:var(--blue)">Agenda Five</b><br><span style="font-size:7px;color:var(--muted)">Sujet principal de la section</span></div></div>
    <div class="num-item"><span class="num">3</span><div><b style="color:var(--blue)">Agenda Three</b><br><span style="font-size:7px;color:var(--muted)">Sujet principal de la section</span></div></div>
    <div class="num-item"><span class="num">6</span><div><b style="color:var(--blue)">Agenda Six</b><br><span style="font-size:7px;color:var(--muted)">Sujet principal de la section</span></div></div>
  </div>
  <footer class="slide-foot">© Copyright 2016 Norvale. Tous droits réservés.</footer>
</section>

<section class="slide fill-blue">
  <div class="photo blue" role="img" aria-label="Bureaux vitrés estompés en fond bleu" style="position:absolute;left:0;right:0;top:0;height:100px;opacity:.5"></div>
  <div class="center-text caps" style="position:absolute;left:24px;right:24px;top:110px;height:140px;font-size:9.5px;line-height:1.5">Malheureusement, peu de gens réussissent à atteindre l'indépendance financière qui leur procurerait un tel niveau de sécurité et de liberté, fortune qui semble être à la portée de presque tous.</div>
  <footer class="slide-foot dark">© Copyright 2016 Norvale. Tous droits réservés.</footer>
</section>

<section class="slide" style="background:var(--white)">
  <div style="position:absolute;left:40px;right:20px;top:14px;font-size:8px;font-weight:700;color:var(--blue);text-align:center">Investissement fixe équivalent à 4$ par jour dans l'indice Atlas 500 de 1965 à 2015, composé sur 50 ans</div>
  <svg viewBox="0 0 340 200" style="position:absolute;left:20px;top:44px;width:340px;height:200px">
    <g stroke="#e3e6ea" stroke-width="1">
      <line x1="30" y1="20" x2="330" y2="20"/><line x1="30" y1="60" x2="330" y2="60"/><line x1="30" y1="100" x2="330" y2="100"/><line x1="30" y1="140" x2="330" y2="140"/><line x1="30" y1="180" x2="330" y2="180"/>
    </g>
    <g font-size="7" fill="#6b7681" font-family="Open Sans,sans-serif">
      <text x="2" y="22">2,0M</text><text x="2" y="62">1,5M</text><text x="2" y="102">1,0M</text><text x="2" y="142">0,5M</text><text x="10" y="182">0</text>
      <text x="30" y="194">1965</text><text x="130" y="194">1985</text><text x="230" y="194">2005</text><text x="305" y="194">2015</text>
    </g>
    <polyline fill="none" stroke="#1d6fb6" stroke-width="2" points="30,180 60,179 90,178 120,176 150,172 180,166 200,158 220,146 240,124 255,108 265,112 275,96 285,70 292,84 300,76 310,50 320,36 330,22"/>
  </svg>
  <footer class="slide-foot">© Copyright 2016 Norvale. Tous droits réservés.</footer>
</section>

<!-- Row 3 -->
<section class="slide fill-blue">
  <div class="center-text" style="position:absolute;left:26px;right:26px;top:20px;bottom:30px;font-size:12px;line-height:1.45">Pourquoi y a-t-il si peu de gens qui sont millionnaires aujourd'hui quand l'équivalent de 4$ par jour d'économies investis dans la bourse de 1950 à 2015 a généré un portefeuille de plus de 1 million de dollars?</div>
  <footer class="slide-foot dark">© Copyright 2016 Norvale. Tous droits réservés.</footer>
</section>

<section class="slide">
  <header class="slide-head"><h2 class="long" style="font-size:12.5px">Les principaux facteurs qui nuisent à l'atteinte de l'indépendance financière:</h2><div class="brand"><span class="dot"></span>NORVALE</div></header>
  <div class="slide-body" style="padding-top:8px">
    <ul class="list">
      <li>L'inaction et le report à plus tard</li>
      <li>Les erreurs émotives (la peur)</li>
      <li>Favoriser les plaisirs à court terme plutôt que les bénéfices à long terme</li>
      <li>Le manque de connaissances</li>
      <li>L'accès à l'information</li>
      <li>Les frais de gestion et la rémunération des conseillers financiers</li>
      <li>Les impôts</li>
      <li>L'inflation</li>
    </ul>
  </div>
  <footer class="slide-foot">© Copyright 2016 Norvale. Tous droits réservés.</footer>
</section>

<section class="slide">
  <div class="photo" role="img" aria-label="Poignée de main entre deux gens d'affaires" style="position:absolute;left:0;top:0;bottom:14px;width:190px"></div>
  <div class="side-panel fill-green" style="left:190px;right:0">
    <div class="brand on-dark" style="margin-bottom:22px"><span class="dot" style="background:var(--white)"></span>NORVALE</div>
    <div style="font-size:15px;font-weight:600;margin-bottom:10px">L'inaction...</div>
    <p style="font-size:9px;line-height:1.45">Vous croyez ne pas avoir les moyens d'épargner?</p>
    <p style="font-size:9px;line-height:1.45">Pour générer 4$ par jour, il ne suffit que de se faire son café et son muffin à la maison le matin au lieu de l'acheter sur la route! Ne parle pas ici d'un grand sacrifice pour pouvoir réaliser nos rêves!</p>
  </div>
  <footer class="slide-foot">© Copyright 2016 Norvale. Tous droits réservés.</footer>
</section>

<!-- Row 4 -->
<section class="slide">
  <header class="slide-head"><h2>Les erreurs émotives (La peur)...</h2><div class="brand"><span class="dot"></span>NORVALE</div></header>
  <div class="slide-body center-text" style="font-size:9.5px;line-height:1.5;padding:0 10px">En 1973 et 1974, la valeur des actions américaines a diminué de 40%. Un investisseur qui avait investi 100$ par mois depuis 1965 a vu son portefeuille passer de 13 300$ à 9 500$. Pris de panique, il vend toutes ses actions pour arrêter l'hémorragie. En 1975, les actions américaines augmentent de 37%. Maintenant tout excité après une telle performance, l'investisseur réinvestit ses 9 500$ l'année suivante. Quel a été l'impact de cette décision?</div>
  <footer class="slide-foot">© Copyright 2016 Norvale. Tous droits réservés.</footer>
</section>

<section class="slide" style="background:var(--white)">
  <div style="position:absolute;left:30px;right:20px;top:12px;font-size:8px;font-weight:700;color:var(--blue);text-align:center">Investissement fixe équivalent à 4$ par jour dans l'indice Atlas 500 avec retrait de 1973-1974 et réinvestissement en 1976</div>
  <div class="note" style="position:absolute;left:80px;top:56px;font-size:9px">Cette seule erreur a coûté 300 000$ !</div>
  <svg viewBox="0 0 340 190" style="position:absolute;left:20px;top:56px;width:340px;height:190px">
    <g stroke="#e3e6ea"><line x1="30" y1="30" x2="330" y2="30"/><line x1="30" y1="80" x2="330" y2="80"/><line x1="30" y1="130" x2="330" y2="130"/><line x1="30" y1="175" x2="330" y2="175"/></g>
    <g font-size="7" fill="#6b7681" font-family="Open Sans,sans-serif"><text x="4" y="32">1,5M</text><text x="4" y="82">1,0M</text><text x="4" y="132">0,5M</text><text x="14" y="177">0</text><text x="30" y="186">1965</text><text x="180" y="186">1990</text><text x="305" y="186">2015</text></g>
    <polyline fill="none" stroke="#1d6fb6" stroke-width="2" points="30,175 80,173 120,170 160,164 190,154 215,138 235,118 250,104 262,108 275,92 288,78 298,88 310,62 330,40"/>
    <polyline fill="none" stroke="#3fae4a" stroke-width="2" points="30,175 80,174 120,172 160,168 190,162 215,152 235,138 250,128 262,131 275,120 288,110 298,116 310,100 330,84"/>
  </svg>
  <footer class="slide-foot">© Copyright 2016 Norvale. Tous droits réservés.</footer>
</section>

<section class="slide" style="background:var(--white)">
  <div style="position:absolute;left:20px;right:20px;top:12px;font-size:8px;font-weight:700;color:var(--green-dark);text-align:center">Rendement annuel minimum, maximum et moyen de l'indice Atlas 500 de 1950 à 2016</div>
  <div style="position:absolute;left:40px;top:40px;width:150px;font-size:6.5px;color:var(--green-dark)">La perte maximale sur une période d'un an a été de 40%, mais le rendement moyen reste positif.</div>
  <div style="position:absolute;right:20px;top:160px;width:120px;font-size:6.5px;color:var(--blue)">Les rendements sur une période de 15 ans sont toujours positifs depuis 1950.</div>
  <svg viewBox="0 0 340 190" style="position:absolute;left:20px;top:56px;width:340px;height:190px">
    <line x1="30" y1="95" x2="330" y2="95" stroke="#c9ced4"/>
    <g stroke="#1d6fb6" stroke-width="2">
      <line x1="60" y1="20" x2="60" y2="170"/><line x1="100" y1="45" x2="100" y2="140"/><line x1="140" y1="60" x2="140" y2="120"/><line x1="180" y1="68" x2="180" y2="112"/><line x1="220" y1="74" x2="220" y2="104"/><line x1="260" y1="78" x2="260" y2="98"/><line x1="300" y1="80" x2="300" y2="94"/>
    </g>
    <g fill="#3fae4a"><circle cx="60" cy="82" r="3"/><circle cx="100" cy="84" r="3"/><circle cx="140" cy="84" r="3"/><circle cx="180" cy="85" r="3"/><circle cx="220" cy="86" r="3"/><circle cx="260" cy="86" r="3"/><circle cx="300" cy="86" r="3"/></g>
    <g font-size="7" fill="#6b7681" font-family="Open Sans,sans-serif"><text x="54" y="185">1 an</text><text x="92" y="185">3 ans</text><text x="132" y="185">5 ans</text><text x="170" y="185">10 ans</text><text x="210" y="185">15 ans</text><text x="250" y="185">20 ans</text><text x="290" y="185">25 ans</text></g>
  </svg>
  <footer class="slide-foot">© Copyright 2016 Norvale. Tous droits réservés.</footer>
</section>

<!-- Row 5 -->
<section class="slide fill-green">
  <div class="photo" role="img" aria-label="Personne consultant des graphiques boursiers, estompée" style="position:absolute;right:0;top:0;bottom:14px;width:120px;opacity:.35"></div>
  <div class="center-text" style="position:absolute;left:20px;right:20px;top:16px;bottom:24px;font-size:9.5px;line-height:1.5">Chaque année, la firme américaine Meridian Research étudie les rendements réalisés par les investisseurs particuliers. Ils ont constaté qu'au moment où le rendement moyen de l'indice boursier américain Atlas 500 au cours des vingt dernières années a été de 10,35%, l'investisseur particulier qui a investi lui aussi dans les actions américaines a réalisé un rendement de 3,66% par année. La firme attribue cette mauvaise performance en grande partie à la mauvaise gestion des émotions et en particulier la peur de perdre.</div>
  <footer class="slide-foot dark">© Copyright 2016 Norvale. Tous droits réservés.</footer>
</section>

<section class="slide">
  <header class="slide-head"><h2>Le manque de connaissances...</h2><div class="brand"><span class="dot"></span>NORVALE</div></header>
  <div class="slide-body">
    <div style="width:180px;margin:16px 0 16px 10px">Les deux grands types de produits dans lesquels on peut investir sont:</div>
    <div class="num-item" style="margin-left:10px"><span class="num">1</span>Les actions</div>
    <div class="num-item" style="margin-left:10px"><span class="num">2</span>Les titres à revenu fixe</div>
    <div class="photo" role="img" aria-label="Gens d'affaires en discussion" style="position:absolute;right:0;top:6px;bottom:6px;width:130px"></div>
  </div>
  <footer class="slide-foot">© Copyright 2016 Norvale. Tous droits réservés.</footer>
</section>

<section class="slide">
  <header class="slide-head"><h2>1. Les titres à revenu fixe</h2><div class="brand"><span class="dot"></span>NORVALE</div></header>
  <div class="slide-body center-text"><p class="big-quote">Quand un gouvernement ou une entreprise a besoin d'argent, il peut soit emprunter à la banque ou soit emprunter directement du grand public. S'il emprunte du public, on dit qu'il émet une obligation...</p></div>
  <footer class="slide-foot">© Copyright 2016 Norvale. Tous droits réservés.</footer>
</section>

<!-- Row 6 -->
<section class="slide">
  <header class="slide-head"><h2>1. Les titres à revenu fixe</h2><div class="brand"><span class="dot"></span>NORVALE</div></header>
  <div class="slide-body center-text"><p class="big-quote">Quand un gouvernement ou une entreprise a besoin d'argent, il peut soit emprunter à la banque ou soit emprunter directement du grand public. S'il emprunte du public, on dit qu'il émet une obligation...</p></div>
  <footer class="slide-foot">© Copyright 2016 Norvale. Tous droits réservés.</footer>
</section>

<section class="slide">
  <header class="slide-head"><h2>1. Les titres à revenu fixe (suite)</h2><div class="brand"><span class="dot"></span>NORVALE</div></header>
  <div class="photo" role="img" aria-label="Silhouettes de gens d'affaires dans un hall" style="position:absolute;left:0;top:45px;bottom:14px;width:150px"></div>
  <div class="fill-blue center-text" style="position:absolute;left:150px;right:0;top:45px;bottom:14px;padding:14px;font-size:9.5px;line-height:1.5">En investissant dans une obligation, vous devenez donc prêteur d'une somme fixe, à un taux d'intérêt généralement fixe et votre argent vous sera remboursé à une date déterminée à l'avance.</div>
  <footer class="slide-foot">© Copyright 2016 Norvale. Tous droits réservés.</footer>
</section>

<section class="slide">
  <header class="slide-head"><h2>1. Les titres à revenu fixe (suite)</h2><div class="brand"><span class="dot"></span>NORVALE</div></header>
  <div class="slide-body" style="padding-top:8px">
    <div style="color:var(--blue);font-weight:600;font-size:11px;margin-bottom:6px">Exemple</div>
    <p>1 000$ Province de Norland 2% 1<sup>er</sup> décembre 2021</p>
    <p>Dans cet exemple, vous prêtez 1 000$ au gouvernement de Norland pour 5 ans.</p>
    <p>Vous recevrez 20$ par année en intérêt. Le gouvernement vous remboursera 1 000$ le 1<sup>er</sup> décembre 2021.</p>
  </div>
  <footer class="slide-foot">© Copyright 2016 Norvale. Tous droits réservés.</footer>
</section>

<!-- Row 7 -->
<section class="slide">
  <header class="slide-head"><h2>1. Les titres à revenu fixe (suite)</h2><div class="brand"><span class="dot"></span>NORVALE</div></header>
  <div class="slide-body">
    <div style="width:190px;margin-top:10px">On classifie les obligations d'investissement relativement sécuritaire car vous prêtez de l'argent seulement à celui qui emprunte l'argent fait faillite (ce qui est assez rare).<br><br>Le rendement est plafonné, mais connu à l'avance.</div>
    <div class="photo" role="img" aria-label="Homme d'affaires marchant dans un bureau" style="position:absolute;right:0;top:6px;bottom:6px;width:140px"></div>
  </div>
  <footer class="slide-foot">© Copyright 2016 Norvale. Tous droits réservés.</footer>
</section>

<section class="slide">
  <header class="slide-head"><h2>1. Les titres à revenu fixe (suite)</h2><div class="brand"><span class="dot"></span>NORVALE</div></header>
  <div class="slide-body center-text"><p class="big-quote" style="font-size:11px">Le prix des obligations fluctue à tous les jours, car on peut les revendre avant la date d'échéance. Vous perdrez une partie de votre capital si les taux d'intérêt ont augmenté depuis votre investissement initial, mais vous encaisserez plus que votre capital si les taux d'intérêt ont baissé depuis votre investissement initial.</p></div>
  <footer class="slide-foot">© Copyright 2016 Norvale. Tous droits réservés.</footer>
</section>

<section class="slide">
  <header class="slide-head"><h2>2. Les actions</h2><div class="brand"><span class="dot"></span>NORVALE</div></header>
  <div class="slide-body">
    <div class="photo" role="img" aria-label="Équipe de professionnels dans une salle de réunion" style="position:absolute;left:0;top:6px;bottom:6px;width:130px"></div>
    <div style="margin-left:145px;margin-top:8px">Pour financer des projets, un propriétaire d'entreprise peut décider de vendre des parts de son entreprise à d'autres investisseurs. Ces parts, ce sont ce que l'on appelle les actions et elles ne sont pas remboursables. Par contre, les actions peuvent être achetées et vendues en tout temps sur le marché des actions que l'on appelle la bourse.</div>
  </div>
  <footer class="slide-foot">© Copyright 2016 Norvale. Tous droits réservés.</footer>
</section>

<!-- Row 8 -->
<section class="slide">
  <header class="slide-head"><h2>2. Les actions (suite)</h2><div class="brand"><span class="dot"></span>NORVALE</div></header>
  <div class="slide-body center-text"><p class="big-quote" style="font-size:10.5px">Le prix des actions fluctue à la hausse ou à la baisse à tous les jours selon l'offre et la demande (décisions souvent émotives) et les performances financières de l'entreprise qui sont divulguées à tous les 3 mois (décisions plus rationnelles).</p></div>
  <footer class="slide-foot">© Copyright 2016 Norvale. Tous droits réservés.</footer>
</section>

<section class="slide">
  <header class="slide-head"><h2>2. Les Actions (suite)</h2><div class="brand"><span class="dot"></span>NORVALE</div></header>
  <div class="slide-body center-text"><p class="big-quote" style="font-size:11px">En général, le rendement des actions est plus élevé que le rendement des obligations, mais beaucoup plus volatil. La possibilité de gain est illimitée, alors que la possibilité de perdre tout notre investissement est possible dans le cas de la faillite de l'entreprise.</p></div>
  <footer class="slide-foot">© Copyright 2016 Norvale. Tous droits réservés.</footer>
</section>

<section class="slide">
  <div class="fill-blue" style="position:absolute;left:0;right:0;top:0;height:40px"></div>
  <div class="photo" role="img" aria-label="Gens d'affaires debout discutant" style="position:absolute;left:16px;top:18px;width:160px;height:130px"></div>
  <div style="position:absolute;left:190px;right:16px;top:56px;font-size:9px;line-height:1.45">On peut investir dans les obligations et les actions en ouvrant l'un des comptes suivants dans une institution financière:</div>
  <div style="position:absolute;left:190px;top:140px;font-size:9px">
    <div class="num-item"><span class="num">1</span>REER</div>
    <div class="num-item"><span class="num">2</span>CELI</div>
    <div class="num-item"><span class="num">3</span>Compte d'investissement</div>
  </div>
  <footer class="slide-foot">© Copyright 2016 Norvale. Tous droits réservés.</footer>
</section>

<!-- Row 9 -->
<section class="slide">
  <header class="slide-head"><h2>L'accès à l'information...</h2><div class="brand"><span class="dot"></span>NORVALE</div></header>
  <div class="slide-body">
    <div style="background:var(--white);border-left:4px solid var(--blue);padding:12px 14px;margin-top:8px;font-size:9.5px;line-height:1.5">L'accès à l'information est primordial afin de prendre des décisions d'investissement rationnelles.<br>Autrement, les décisions seront basées sur des conclusions émotives ou erronées qui coûteront cher! Une bonne manière de détecter le manque d'information dans une décision, c'est la présence des mots: « Je pense que »!</div>
  </div>
  <footer class="slide-foot">© Copyright 2016 Norvale. Tous droits réservés.</footer>
</section>

<section class="slide">
  <header class="slide-head"><h2>L'accès à l'information... (suite)</h2><div class="brand"><span class="dot"></span>NORVALE</div></header>
  <div class="slide-body center-text"><p class="big-quote" style="font-size:10.5px">Les principales sources d'informations sont les rapports annuels des entreprises et des gouvernements. Disponibles en ligne ou en format papier, ils contiennent toute l'information sur la santé financière nécessaire à la prise de décision rationnelle.</p></div>
  <footer class="slide-foot">© Copyright 2016 Norvale. Tous droits réservés.</footer>
</section>

<section class="slide">
  <header class="slide-head"><h2>L'accès à l'information... (suite)</h2><div class="brand"><span class="dot"></span>NORVALE</div></header>
  <div class="photo" role="img" aria-label="Personne travaillant sur un ordinateur portable" style="position:absolute;left:0;top:45px;bottom:14px;width:170px"></div>
  <div style="position:absolute;left:186px;right:16px;top:90px;font-size:9.5px;line-height:1.5">Cependant, la technologie nous offre de nos jours des moyens beaucoup plus efficaces, mais beaucoup plus coûteux pour traiter une quantité phénoménale d'informations rapidement.</div>
  <footer class="slide-foot">© Copyright 2016 Norvale. Tous droits réservés.</footer>
</section>

<!-- Row 10 -->
<section class="slide">
  <header class="slide-head"><h2>Les frais de gestion...</h2><div class="brand"><span class="dot"></span>NORVALE</div></header>
  <div class="slide-body">
    <div style="width:200px;font-size:8.5px">Les frais de gestion peuvent réduire significativement ou même annuler complètement le rendement de certains investissements, surtout celui des obligations.<br><br>En effet, le rendement des obligations tourne autour de 1,5% présentement et les fonds mutuels « équilibrés » chargent généralement un frais de gestion annuel supérieur à 2%!!</div>
    <div class="fill-green" style="position:absolute;right:0;top:10px;width:130px;height:130px;padding:8px">
      <div class="photo" role="img" aria-label="Calculatrice et documents financiers" style="width:100%;height:100%"></div>
    </div>
  </div>
  <footer class="slide-foot">© Copyright 2016 Norvale. Tous droits réservés.</footer>
</section>

<section class="slide">
  <header class="slide-head"><h2>Les frais de gestion... (suite)</h2><div class="brand"><span class="dot"></span>NORVALE</div></header>
  <div class="slide-body">
    <div style="display:grid;grid-template-columns:110px 1fr 1fr;gap:10px 8px">
      <div style="font-weight:600;font-size:8.5px">Quelle est la structure de rémunération des conseillers en placement?</div>
      <div class="icon-item"><span class="num">$</span>Ils sont généralement payés par les firmes de courtage</div>
      <div class="icon-item"><span class="num">%</span>Ils sont également payés à un bonus en fin d'année</div>
      <div style="font-size:8.5px;margin-top:14px">1. Conseillers à salaire fixe plus bonus</div>
      <div class="icon-item"><span class="num">✓</span>Le bonus dépend du volume d'actifs sous gestion</div>
      <div class="icon-item"><span class="num">→</span>Leurs revenus sont liés aux frais de gestion chargés aux clients</div>
    </div>
  </div>
  <footer class="slide-foot">© Copyright 2016 Norvale. Tous droits réservés.</footer>
</section>

<section class="slide">
  <header class="slide-head"><h2 class="long">Quelle est la structure de rémunération des conseillers en placement? (suite)</h2><div class="brand"><span class="dot"></span>NORVALE</div></header>
  <div class="slide-body" style="display:flex;gap:12px;padding-top:10px">
    <div style="width:110px;font-size:8.5px">2. Conseillers à commissions seulement</div>
    <div style="flex:1">
      <div class="icon-item" style="margin-bottom:12px"><span class="num green">$</span>Ce sont généralement les conseillers financiers œuvrant dans les firmes de courtage de plein exercice telles que Banque Laurentis, Valmont Valeurs, Groupe Castel, etc.</div>
      <div class="icon-item"><span class="num green">%</span>Ils ont accès à tous les produits financiers ou presque mais la commission est plus élevée sur certains produits.</div>
    </div>
  </div>
  <footer class="slide-foot">© Copyright 2016 Norvale. Tous droits réservés.</footer>
</section>

<!-- Row 11 -->
<section class="slide">
  <header class="slide-head"><h2 class="long">Quelle est la structure de rémunération des conseillers en placement? (suite)</h2><div class="brand"><span class="dot"></span>NORVALE</div></header>
  <div class="slide-body" style="padding-top:8px">
    <p>2- Conseillers à commissions seulement (suite)</p>
    <p>Ils touchent une quote-part variant de 20% à 60% des frais chargés à leurs clients.</p>
    <p>Autrement dit, lorsque 1 000$ de frais sont chargés au client, un montant variant entre 200$ et 600$ est remis au conseiller. La différence est conservée par l'employeur.</p>
  </div>
  <footer class="slide-foot">© Copyright 2016 Norvale. Tous droits réservés.</footer>
</section>

<section class="slide">
  <header class="slide-head"><h2 class="long" style="font-size:12.5px">Les changements qui affectent l'industrie présentement</h2><div class="brand"><span class="dot"></span>NORVALE</div></header>
  <div class="slide-body" style="font-size:8.5px;padding-top:4px">
    <p>1 - Vague de modifications concernant la rémunération des conseillers en placement des firmes de courtage de plein exercice</p>
    <p>En chiffres, les principaux changements sont:</p>
    <ul class="list">
      <li>La nécessité de produire 450 000$ de frais annuellement au lieu de 300 000$ afin d'obtenir une quote-part supérieure à 20%</li>
      <li>Réduction jusqu'à 75% de la rémunération des conseillers lorsqu'ils conseillent des familles ayant moins de 250 000$ d'investissements</li>
    </ul>
  </div>
  <footer class="slide-foot">© Copyright 2016 Norvale. Tous droits réservés.</footer>
</section>

<section class="slide">
  <header class="slide-head"><h2 class="long" style="font-size:12.5px">Les changements qui affectent l'industrie présentement (suite)</h2><div class="brand"><span class="dot"></span>NORVALE</div></header>
  <div class="slide-body" style="font-size:8.5px;padding-top:6px">
    <ul class="list">
      <li>Ces modifications diminueront fort probablement le nombre de conseillers financiers dans l'industrie rendant ainsi l'accès aux conseillers restants plus difficile</li>
      <li>Une expérience similaire a fait diminuer le nombre de conseillers financiers de 22% au Royaume-Uni de 40 000 en 2011 à 31 000 en 2013 selon une étude de Ashford Business School</li>
    </ul>
  </div>
  <footer class="slide-foot">© Copyright 2016 Norvale. Tous droits réservés.</footer>
</section>

<!-- Row 12 -->
<section class="slide">
  <header class="slide-head"><h2 class="long" style="font-size:12.5px">Les changements qui affectent l'industrie présentement (suite)</h2><div class="brand"><span class="dot"></span>NORVALE</div></header>
  <div class="slide-body" style="font-size:8.5px;padding-top:4px">
    <p>2- Introduction d'une nouvelle réglementation</p>
    <ul class="list" style="margin-top:6px">
      <li>À partir de 2017, les clients recevront un rapport annuel présentant la somme, payée l'année précédente, de tous les frais dont certains étaient auparavant « cachés »!</li>
      <li>Les clients recevront également un rapport sur la performance de leur portefeuille</li>
    </ul>
  </div>
  <footer class="slide-foot">© Copyright 2016 Norvale. Tous droits réservés.</footer>
</section>

<section class="slide">
  <header class="slide-head"><h2 class="long" style="font-size:12.5px">Les changements qui affectent l'industrie présentement (suite)</h2><div class="brand"><span class="dot"></span>NORVALE</div></header>
  <div class="slide-body center-text"><p class="big-quote" style="font-size:10px">Ces nouvelles exigences constituent une réelle révolution dans le domaine de la gestion de placement. Bon nombre des frais étaient historiquement cachés aux yeux des clients et la performance donnée sur demande seulement. Cela causera une grande surprise pour une bonne partie d'entre eux lorsque l'information leur sera enfin dévoilée au début de 2017!</p></div>
  <footer class="slide-foot">© Copyright 2016 Norvale. Tous droits réservés.</footer>
</section>

<section class="slide">
  <header class="slide-head"><h2>Les impôts...</h2><div class="brand"><span class="dot"></span>NORVALE</div></header>
  <div class="fill-blue" style="position:absolute;left:0;right:0;top:56px;bottom:14px;padding:14px 18px;font-size:9.5px;line-height:1.5">
    <p>Il n'y a aucun impôt à payer pour les investissements faits dans un REER, mais les montants retirés du REER sont imposables comme un revenu de travail.</p>
    <p style="margin-top:14px">Il n'y a aucun impôt à payer pour les investissements faits dans un CELI. Les montants retirés ne sont pas imposables non plus, mais il y a une limite de cotisation de 5 500$ par année dans un CELI.</p>
  </div>
  <footer class="slide-foot">© Copyright 2016 Norvale. Tous droits réservés.</footer>
</section>

<!-- Row 13 -->
<section class="slide">
  <header class="slide-head"><h2>Les impôts...</h2><div class="brand"><span class="dot"></span>NORVALE</div></header>
  <div class="fill-blue" style="position:absolute;left:0;top:56px;bottom:14px;width:110px;padding:12px;font-size:8px;line-height:1.45">Pour les investissements faits dans un compte d'investissement régulier, les taux maximum d'impôt appliqués sur les investissements pour un particulier gagnant 55 000$ par année sont les suivants:</div>
  <div style="position:absolute;left:120px;right:10px;top:80px;display:grid;grid-template-columns:repeat(3,1fr);gap:8px;text-align:center;font-size:6.5px;line-height:1.3">
    <div><svg viewBox="0 0 40 40" width="46" height="46"><circle cx="20" cy="20" r="15" fill="none" stroke="#e1e5e9" stroke-width="7"/><circle cx="20" cy="20" r="15" fill="none" stroke="#1d6fb6" stroke-width="7" stroke-dasharray="35.6 94.2" transform="rotate(-90 20 20)"/></svg><div style="font-weight:700;color:var(--blue);font-size:9px">37,12%</div>sur les intérêts des obligations payés à tous les ans</div>
    <div><svg viewBox="0 0 40 40" width="46" height="46"><circle cx="20" cy="20" r="15" fill="none" stroke="#e1e5e9" stroke-width="7"/><circle cx="20" cy="20" r="15" fill="none" stroke="#3fae4a" stroke-width="7" stroke-dasharray="16.5 94.2" transform="rotate(-90 20 20)"/></svg><div style="font-weight:700;color:var(--green-dark);font-size:9px">17,43%</div>sur les revenus de dividende des actions payés à tous les ans</div>
    <div><svg viewBox="0 0 40 40" width="46" height="46"><circle cx="20" cy="20" r="15" fill="none" stroke="#e1e5e9" stroke-width="7"/><circle cx="20" cy="20" r="15" fill="none" stroke="#1d6fb6" stroke-width="7" stroke-dasharray="17.5 94.2" transform="rotate(-90 20 20)"/></svg><div style="font-weight:700;color:var(--blue);font-size:9px">18,56%</div>sur les gains en capital payés dans l'année où le gain est réalisé</div>
  </div>
  <footer class="slide-foot">© Copyright 2016 Norvale. Tous droits réservés.</footer>
</section>

<section class="slide fill-blue">
  <div class="photo blue" role="img" aria-label="Gens d'affaires dans un hall de verre, estompés" style="position:absolute;left:0;right:0;top:0;height:120px;opacity:.55"></div>
  <div style="position:absolute;left:0;right:0;top:140px;text-align:center;font-size:18px;font-weight:600">Les impôts...</div>
  <div style="position:absolute;left:30px;right:30px;top:180px;text-align:center;font-size:10px;line-height:1.5">Parfois, les taux d'imposition peuvent être de plus de 100% sans que l'on s'en aperçoive!</div>
  <footer class="slide-foot dark">© Copyright 2016 Norvale. Tous droits réservés.</footer>
</section>

<section class="slide">
  <div class="side-panel fill-blue" style="left:0;width:170px;padding:14px">
    <div style="background:var(--white);padding:6px 8px;margin-bottom:20px"><div class="brand"><span class="dot"></span>NORVALE</div></div>
    <div style="font-size:12px;font-weight:600;margin-bottom:10px">Our Contact</div>
    <div style="font-size:7.5px;line-height:1.4">
      <div style="display:flex;gap:6px;align-items:center;margin-bottom:6px"><svg width="12" height="12" viewBox="0 0 12 12"><path d="M6 1a3.5 3.5 0 0 0-3.5 3.5C2.5 7.5 6 11 6 11s3.5-3.5 3.5-6.5A3.5 3.5 0 0 0 6 1z" fill="#fff"/><circle cx="6" cy="4.5" r="1.2" fill="#1d6fb6"/></svg>120 rue Principale, Ville, QC</div>
      <div style="display:flex;gap:6px;align-items:center;margin-bottom:6px"><svg width="12" height="12" viewBox="0 0 12 12"><path d="M3 1.5l2 2-1 1.2a6 6 0 0 0 3.3 3.3l1.2-1 2 2-1.2 1.5C5.5 10.5 1.5 6.5 1.5 2.7z" fill="#fff"/></svg>(555) 010-0199</div>
      <div style="display:flex;gap:6px;align-items:center;margin-bottom:6px"><svg width="12" height="12" viewBox="0 0 12 12"><rect x="1" y="2.5" width="10" height="7" fill="#fff"/><path d="M1 2.5l5 4 5-4" fill="none" stroke="#1d6fb6"/></svg>info@norvale.example</div>
      <div style="display:flex;gap:6px;align-items:center"><svg width="12" height="12" viewBox="0 0 12 12"><circle cx="6" cy="6" r="5" fill="none" stroke="#fff"/><path d="M1 6h10M6 1c-2 3-2 7 0 10M6 1c2 3 2 7 0 10" fill="none" stroke="#fff" stroke-width=".8"/></svg>www.norvale.example</div>
    </div>
  </div>
  <div style="position:absolute;left:184px;right:14px;top:16px">
    <div style="font-size:14px;font-weight:600;color:var(--blue);margin-bottom:8px">L'équipe...</div>
    <div style="font-size:8px;font-weight:600;margin-bottom:8px">Julien Marchand, CFA, Pl. Fin.</div>
    <ul class="list" style="font-size:7.5px;line-height:1.35">
      <li>Gestionnaire de portefeuille certifié (détenteur du titre CFA)</li>
      <li>Chargé de cours à l'université en finance de la gestion de portefeuille</li>
      <li>Planificateur financier</li>
      <li>Plus de 15 ans d'expérience dans le domaine des services financiers</li>
    </ul>
  </div>
  <footer class="slide-foot">© Copyright 2016 Norvale. Tous droits réservés.</footer>
</section>

</main>
</body>
</html>
```